Morenzo - A new California agave spirit brand needs a label!

Hello designers! We had a lot of fun with our last project getting our logo design, now we need to put that logo onto a label!

Morenzo is a company that makes agave spirit (aka Tequila but we can't call it that because of regional laws) from California grown agaves. Our goal is to make a premium quality that goes head to head with some of the best tequilas in the world, and we need a package that conveys that.

The label that we want will be sophisticated and bold that will stand out on a shelf and be recognizable from across a bar. It needs to convey its premium status just from a glance.

Please do not use colors other than white, black, and sky/electric blue. The color scheme I see most likely winning will be some sort of white/offwhite background with black lettering, with possibly an accent of blue.

I will supply the winning logo artwork from the last contest, but if you have a better logo in mind feel free to create something new.

Please look at the link provided below for examples of the highest rated blanco tequilas.

https://www.pourfinderguide.example/agave_spirits/blanco?q=&hPP=30&idx=BaseProduct&p=0&dFR%5Bcategory%5D%5B0%5D=Blanco

Please reference the LKR documents attached on mandatory label requirements.
Use this link for descriptions of each element of an alcohol label: https://www.lkr.example/ds-labeling-home/anatomy-of-a-distilled-spirits-label-tool

Our label must have these elements:

Brand Name: Morenzo
Class/Type Description: California Agave Spirit
Fanciful Name: Blanco
Alcohol Content: 40% ABV
Government Warning
Name and Address: Distilled and Bottled by Morenzo Spirits, Durham, CA
Net Contents: 750 ml
Barcode
Website: www.morenzospirits.example
Please leave a space for a brief paragraph on the back of the bottle

Thank you and good luck!

Target Market(s)

Premium Tequila Drinkers

Industry/Entity Type

Distilled Spirits

Colors

Designer to choose colors to be used in the design.

Requirements
Must have
• Please reference the LKR documents provided on required label information.

```html
<!DOCTYPE html>
<html lang="en">
<head>
<meta charset="utf-8">
<title>Morenzo — California Agave Spirit Blanco Label</title>
<link rel="stylesheet" href="https://fonts.googleapis.com/css2?family=IM+Fell+French+Canon+SC&family=IM+Fell+English&family=Josefin+Sans:wght@400&display=swap">
<style>
  :root {
    --paper: #f3f4f4;
    --paper-edge: #e9eaeb;
    --ink: #111111;
    --sky: #4bb8ea;
    --illustration-grey: #8c8c8c;
  }
  * { margin: 0; padding: 0; box-sizing: border-box; }
  html, body { width: 800px; height: 1200px; overflow: hidden; background: var(--paper); }
  .label {
    position: relative;
    width: 800px;
    height: 1200px;
    overflow: hidden;
    background: radial-gradient(ellipse at 50% 45%, #f8f8f8 0%, var(--paper) 60%, var(--paper-edge) 100%);
    color: var(--ink);
  }
  .leaf-decor { position: absolute; }
  .leaf-decor--top-right { left: 508px; top: 0; width: 292px; height: 390px; }
  .leaf-decor--bottom-left { left: 0; top: 813px; width: 233px; height: 387px; }

  .brand {
    position: absolute;
    left: 0; top: 68px; width: 800px;
    display: flex; flex-direction: column; align-items: center;
  }
  .brand__mark {
    width: 116px; height: 116px;
    border: 4px solid var(--ink);
    border-radius: 50%;
  }
  .brand__name {
    margin-top: 20px;
    font-family: "Josefin Sans", sans-serif;
    font-weight: 400;
    font-size: 38px;
    letter-spacing: 7px;
    line-height: 1;
    padding-left: 7px;
    color: var(--ink);
  }

  .agave-illustration {
    position: absolute;
    left: 174px; top: 267px; width: 454px; height: 343px;
  }

  .rule {
    position: absolute;
    left: 174px; width: 452px; height: 1.5px;
    background: var(--ink);
  }
  .rule--upper { top: 649px; }
  .rule--lower { top: 881px; }

  .class-type {
    position: absolute;
    left: 0; top: 682px; width: 800px;
    text-align: center;
    font-family: "IM Fell French Canon SC", serif;
    font-weight: 400;
    font-size: 80px;
    line-height: 90px;
    letter-spacing: -1px;
    color: var(--ink);
    -webkit-text-stroke: 2px var(--ink);
  }

  .fanciful {
    position: absolute;
    left: 0; top: 918px; width: 800px;
    text-align: center;
    font-family: "IM Fell French Canon SC", serif;
    font-weight: 400;
    font-size: 96px;
    line-height: 104px;
    letter-spacing: 1px;
    color: var(--ink);
    -webkit-text-stroke: 2.5px var(--ink);
  }

  .contents {
    position: absolute;
    left: 0; top: 1078px; width: 800px;
    text-align: center;
    font-family: "IM Fell English", serif;
    font-size: 25px;
    line-height: 36px;
    color: var(--ink);
    -webkit-text-stroke: 0.6px var(--ink);
  }
</style>
</head>
<body>
  <main class="label">
    <svg class="leaf-decor leaf-decor--top-right" viewBox="0 0 292 390" role="img" aria-label="Faint sky-blue engraved agave leaves reaching in from the top right corner">
      <defs>
        <linearGradient id="leafFadeTop" x1="1" y1="0" x2="0" y2="1">
          <stop offset="0" stop-color="#4bb8ea" stop-opacity="0.35"/>
          <stop offset="1" stop-color="#4bb8ea" stop-opacity="0.05"/>
        </linearGradient>
      </defs>
      <path d="M292 0 L292 390 C250 300 200 250 150 280 C200 200 240 150 160 200 C200 130 250 80 100 40 C180 30 240 10 292 0 Z" fill="url(#leafFadeTop)"/>
    </svg>

    <svg class="leaf-decor leaf-decor--bottom-left" viewBox="0 0 233 387" role="img" aria-label="Faint sky-blue engraved agave leaves reaching in from the bottom left corner">
      <defs>
        <linearGradient id="leafFadeBottom" x1="0" y1="1" x2="1" y2="0">
          <stop offset="0" stop-color="#4bb8ea" stop-opacity="0.32"/>
          <stop offset="1" stop-color="#4bb8ea" stop-opacity="0.04"/>
        </linearGradient>
      </defs>
      <path d="M0 0 C30 80 40 160 60 220 C100 160 140 110 165 80 C150 160 120 230 90 290 C140 290 190 280 233 275 C180 320 120 360 60 387 L0 387 Z" fill="url(#leafFadeBottom)"/>
    </svg>

    <header class="brand">
      <div class="brand__mark" aria-hidden="true"></div>
      <p class="brand__name">MORENZO</p>
    </header>

    <svg class="agave-illustration" viewBox="0 0 454 343" role="img" aria-label="Black ink engraving of an agave plant with spiky upright leaves">
      <defs>
        <radialGradient id="agaveTone" cx="0.5" cy="0.65" r="0.55">
          <stop offset="0" stop-color="#8c8c8c" stop-opacity="0.55"/>
          <stop offset="0.7" stop-color="#8c8c8c" stop-opacity="0.2"/>
          <stop offset="1" stop-color="#8c8c8c" stop-opacity="0"/>
        </radialGradient>
      </defs>
      <rect width="454" height="343" fill="url(#agaveTone)"/>
    </svg>

    <div class="rule rule--upper"></div>

    <h1 class="class-type">CALIFORNIA<br>AGAVE SPIRIT</h1>

    <div class="rule rule--lower"></div>

    <h2 class="fanciful">BLANCO</h2>

    <p class="contents">40% Alc. By Vol.<br>750 ml</p>
  </main>
</body>
</html>
```